School Hallway Magnetic Display Design for school values

I am looking for a someone to help me design a magnetic hallway display that will hang in the hallway of our small school. There are several elements, including 1. 6ft by 4ft designed magnetic bulletin board, 2. Magnets that will stick to the board. See attachment for which elements belong where. The display will be for our TRAVEK program, which rewards students for demonstrating our school values. We want the display to be beautiful and interactive. We are also rebranding, so we want the design to align with our new fonts and colors. In the attached PDF is an outline of our new brand guidelines. Unfortunately, we don't have the color codes, but I'm hoping that you can match the colors listed. Attached are elements to be used on the board, but please use your creativity to make it more dynamic and visually appealing. For example, the star magnets could be another shape. The TRAVEK magnets must remain the same. I've included two photos of boards at other schools that inspired this project.

Target Market(s)

School Community

Industry/Entity Type

Education

Requirements
Should not have
• School Logo

```html
<!DOCTYPE html>
<html lang="en">
<head>
<meta charset="utf-8">
<title>TRAVEK of The Month – Hallway Display</title>
<link href="https://fonts.googleapis.com/css2?family=Pathway+Gothic+One&display=swap" rel="stylesheet">
<style>
  :root {
    --navy: #234f70;
    --cream: #f8f7f0;
    --yellow: #fdd873;
    --coral: #e08a72;
    --lilac: #bc9cc7;
    --sage: #d5dfb2;
    --sky: #b3cee7;
    --royal: #244e8f;
    --tube: #2d5d96;
    --ink: #111111;
    --white: #ffffff;
  }
  * { box-sizing: border-box; margin: 0; padding: 0; }
  html, body { width: 1200px; height: 600px; overflow: hidden; background: var(--white); }
  .canvas { position: relative; width: 1200px; height: 600px; background: var(--white); }

  .star { position: absolute; width: 62px; height: 60px; }
  .star svg { width: 100%; height: 100%; display: block; }

  .board {
    position: absolute; left: 241px; top: 60px; width: 725px; height: 484px;
  }
  .board-frame {
    position: absolute; inset: 0;
    background:
      linear-gradient(90deg, var(--yellow) 0%, var(--coral) 45%, var(--lilac) 100%) top / 100% 50% no-repeat,
      linear-gradient(90deg, var(--sky) 0%, var(--royal) 50%, var(--sage) 100%) bottom / 100% 50% no-repeat;
  }
  .board-frame::after {
    content: ""; position: absolute; inset: 0;
    background: var(--navy); opacity: 0.45;
  }
  .board-panel {
    position: absolute; left: 26px; top: 25px; width: 674px; height: 433px;
    background: var(--cream);
  }
  .title-pill {
    position: absolute; left: 0; top: 10px; width: 283px; height: 59px;
    background: var(--navy);
    border: 3px solid var(--coral); border-left: none;
    border-radius: 0 30px 30px 0;
    display: flex; align-items: center; justify-content: center;
    padding-right: 10px;
    color: var(--yellow);
    font-family: "Pathway Gothic One", sans-serif; font-size: 38px; line-height: 1;
    white-space: nowrap;
  }
  .thermometer {
    position: absolute; left: 542px; top: 45px; width: 109px; height: 344px;
    border-radius: 40px 40px 55px 55px;
    background: linear-gradient(180deg, var(--tube) 0%, var(--tube) 50%, var(--coral) 100%);
  }

  .value-magnet {
    position: absolute; left: 981px; width: 211px; height: 60px;
  }
  .value-magnet .magnet-frame { position: absolute; inset: 0; }
  .value-magnet .magnet-label {
    position: absolute; left: 15px; top: 15px; width: 169px; height: 31px;
    background: var(--cream);
    display: flex; align-items: center; justify-content: center;
    font-family: "Pathway Gothic One", sans-serif; font-size: 28px; line-height: 1;
    color: var(--ink); white-space: nowrap;
  }
  .simplicity .magnet-frame { background: var(--yellow); }
  .integrity .magnet-frame { background: var(--coral); }
  .peace .magnet-frame { background: var(--lilac); }
  .stewardship .magnet-frame { background: var(--sage); }
  .equality .magnet-frame { background: var(--sky); }
  .community .magnet-frame { background: var(--royal); }
</style>
</head>
<body>
<div class="canvas">

  <svg width="0" height="0" style="position:absolute">
    <defs>
      <symbol id="star-shape" viewBox="0 0 100 96">
        <polygon points="50,0 62,36 100,37 70,60 81,96 50,75 19,96 30,60 0,37 38,36" fill="var(--yellow)"/>
        <polygon points="50,0 50,48 62,36" fill="var(--coral)"/>
        <polygon points="100,37 50,48 70,60" fill="var(--coral)"/>
        <polygon points="81,96 50,48 50,75" fill="var(--coral)"/>
        <polygon points="19,96 50,48 30,60" fill="var(--coral)"/>
        <polygon points="0,37 50,48 38,36" fill="var(--coral)"/>
      </symbol>
    </defs>
  </svg>

  <div class="star" style="left:29px;top:74px"><svg><use href="#star-shape"/></svg></div>
  <div class="star" style="left:151px;top:73px"><svg><use href="#star-shape"/></svg></div>
  <div class="star" style="left:29px;top:173px"><svg><use href="#star-shape"/></svg></div>
  <div class="star" style="left:151px;top:172px"><svg><use href="#star-shape"/></svg></div>
  <div class="star" style="left:29px;top:272px"><svg><use href="#star-shape"/></svg></div>
  <div class="star" style="left:151px;top:271px"><svg><use href="#star-shape"/></svg></div>
  <div class="star" style="left:29px;top:372px"><svg><use href="#star-shape"/></svg></div>
  <div class="star" style="left:151px;top:371px"><svg><use href="#star-shape"/></svg></div>
  <div class="star" style="left:29px;top:471px"><svg><use href="#star-shape"/></svg></div>
  <div class="star" style="left:151px;top:470px"><svg><use href="#star-shape"/></svg></div>

  <div class="board">
    <div class="board-frame" role="img" aria-label="Key-pattern border in navy with yellow, coral, lilac, sage and blue sections"></div>
    <div class="board-panel">
      <div class="title-pill">TRAVEK of The Month</div>
      <div class="thermometer" role="img" aria-label="Thermometer illustration in blue with a coral bulb and tick marks"></div>
    </div>
  </div>

  <div class="value-magnet simplicity" style="top:60px">
    <span class="magnet-frame" role="img" aria-label="Yellow key-pattern magnet border"></span>
    <span class="magnet-label">SIMPLICITY</span>
  </div>
  <div class="value-magnet integrity" style="top:145px">
    <span class="magnet-frame" role="img" aria-label="Coral key-pattern magnet border"></span>
    <span class="magnet-label">INTEGRITY</span>
  </div>
  <div class="value-magnet peace" style="top:230px">
    <span class="magnet-frame" role="img" aria-label="Lilac key-pattern magnet border"></span>
    <span class="magnet-label">PEACE</span>
  </div>
  <div class="value-magnet stewardship" style="top:314px">
    <span class="magnet-frame" role="img" aria-label="Sage key-pattern magnet border"></span>
    <span class="magnet-label">STEWARDSHIP</span>
  </div>
  <div class="value-magnet equality" style="top:398px">
    <span class="magnet-frame" role="img" aria-label="Light blue key-pattern magnet border"></span>
    <span class="magnet-label">EQUALITY</span>
  </div>
  <div class="value-magnet community" style="top:483px">
    <span class="magnet-frame" role="img" aria-label="Royal blue key-pattern magnet border"></span>
    <span class="magnet-label">COMMUNITY</span>
  </div>

</div>
</body>
</html>
```